Vendro Sahel - Website Design Brief

Web Design Brief

VENDRO SAHEL
WEBSITE DESIGN BRIEF

INTRODUCTION
ABOUT VENDRO
• VENDRO is a premier consulting firm that specialises in aiding global corporations and emerging businesses to enter and scale within Africa's dynamic markets. Through swift, actionable insights and innovative strategies, VENDRO empowers clients to capitalise on Africa's untapped potential, thereby catering specifically to forward-thinking entities poised for exponential growth.

TASK DESCRIPTION
• Develop a 5-page website for VENDRO.
• The primary goal is to present a clear and concise picture of our consulting firm, its Africa-centric experience, and its offerings to multinational clients looking for a professional partner to penetrate African markets or reclaim lost market share.

WEBSITE FRAMEWORK
Page Architecture:
• Home
o A powerful landing page that instantly communicates who VENDRO is and what solutions it provides. Incorporate impactful visuals and calls-to-action.
• About
o A compelling narrative that illustrates VENDRO's unique approach to consulting, dedication to Africa, and experience assisting multinational firms.
• Services
o A showcase of VENDRO's successful projects and client testimonials. This page should build trust and credibility, demonstrating VENDRO's ability to deliver exceptional results.
• Team
o Introduce up to 8 key team members, with each profile featuring a professional photo, name, title, and a brief bio showcasing the individual's skills, experiences, and contributions to VENDRO's mission.
• Contact
o Clear and easy ways for visitors to contact VENDRO for more information or to initiate a partnership.
• Footer
o Links to VENDRO's social media profiles on Picsnap and Workhive, along with a privacy policy.
o Social links
o Picsnap: https://www.instagram.com/vendrosahel/
o Workhive: https://www.linkedin.com/company/vendrosahel/
o Privacy Policy
o Insert placeholder "lorem ipsum" text.
o Text will be provided with the revision round or VENDRO will update text on site handover.

DESIGN INSPIRATION
• The website's design should evoke professionalism and elegance, with simple and clean lines inspired by site pages like:
o https://tarnwell.example/
o https://tarnwell.example/services/
o One aspect we particularly appreciate is how visitors can easily navigate by scrolling down to find what they're looking for and see everything they need to in an intuitive way on the home page
o What we don’t like about this site is how they navigate from the home page to other random pages – we like about to take you to the about page, and so on.

Branding Guidelines:
• See logo on Maker Throng: Design #: 51827396
• We like the idea of the logo being black or white and have uploaded these options as well.
• Monochrome themes, with spots or splash of colour to highlight something is a style we appreciate.

Website Objectives and Goals:
• Our website's primary goal is to create a strong online presence, acting as a hub for potential clients to discover our credibility, reliability, and our ability to deliver exceptional results. It's essential that our website portrays professionalism, instils trustworthiness, and showcases our sincere dedication to Africa.

Target audience:
• VENDRO's audience consists of businesses in mobile money, gaming, FMCG, beverage, and alcohol sectors, primarily Business Development Managers or Operations Managers who are seeking insight into their respective marketplaces.

Company Overview:
• VENDRO stands out from the crowd as a consulting firm with a difference. Our dynamic team is fully dedicated to one mission: brand development within Africa.
• Unlike other companies that focus solely on online connectivity, we recognize the tremendous value in embracing the vibrant street culture that makes Africa so unique. Community engagement, empowerment, and expansion are at the forefront of everything we do.
• we recognize that unlocking business growth starts with a deep understanding of consumer behavior. It is this understanding that bridges the gap between companies and the communities that drive the cash economy. Our purpose is to reconnect businesses with the vibrant pulse of these essential local markets, injecting fresh vitality into their brands and propelling them towards resounding success in Africa.

Development to include:
• Basic SEO Setup:
o The website should be optimized for search engines, incorporating keywords, meta tags, and alt tags for images.
• Searchly Metrics Setup.
o To track website traffic and user behaviour for ongoing optimization.
• Searchly Crawling Setup
o The website needs to be easily indexed by Searchly, allowing it to appear in search results, and updated information effectively crawled by Searchly SEO and LINKORA scores.

PAGE CONTENT:
Home Page
• Background
o Option #1
o 4K video on home page, running on loop
o Bold Statement Text over Video
o Option #2
o Still Image
o Animated text making bold statement (e.g. our motto)

• Sections
o Contrast colour blocks or a way of making it clear that the next topic is a new topic.
o 5 sections
1. Home Main - Video + bold statement text
2. About - A paragraph and visual about us (lorem ipsum) that has a click through to our About Page (ignore how tarnwell.example navigate, we think this is too complicated for our needs)
3. Services – communicated in some simple and powerful ways (we leave this open to you) – but keeping in mind it needs to be concise and professional.
4. Other - Something about our process that makes us unique (lorem ipsum text) and a placeholder image/animation.
5. Contact – a call-to-action button that takes you to our contact, but showcases a mobile number and email address.
6. Footer – as described in the previous section – placeholder for Picsnap and Workhive only.

About Page
• Don’t reference tarnwell.example for this page.
• Main Section
o Bold statements and images
• History Section
o A story about us and our past
• Final Section
o Some of our comments and final thoughts

Services Page
• How https://tarnwell.example/services/ is laid out is great – we prefer a light theme.
• 6 - 8 x icons with headings and a brief description text box, and a read more drop down – all as placeholders to be edited later.
• For ease of direction for this page, look to the link shared above.

Team
• Add Placeholders for up to 8 team members (we only have 4 now):
o Image placeholder
o Name placeholder
o Title placeholder
o Short Bio (lorem ipsum)

Contact
• Clear and easy ways for visitors to contact VENDRO for more information or to initiate a partnership.

• Insert placeholder "lorem ipsum" text, we will provide the text with our revision round.
o Ideally an easy form process that gives the user some options or dropdowns to complete before submission – up to 3 would be sufficient.
o Require their name and contact details.

NOTE: Images to follow:

Target Market(s)

VENDRO's audience consists of businesses in mobile money, gaming, FMCG, beverage, and alcohol sectors, primarily Business Development Managers or Operations Managers who are seeking insight into their respective marketplaces.

Industry/Entity Type

VENDRO is a premier consulting firm that specialises in aiding global corporations and emerging businesses to enter and scale within Africa's dynamic markets

Coding

Coded - Design and coding required

Number of Pages Required

5+ page

Font styles to use
Sans Serif
Other font styles liked:
• Poppins Font Family

Colors

Designer to choose colors to be used in the design.

Requirements
Must have
• The primary goal is to present a clear and concise picture of our consulting firm, and it's specialisation in Africa - smooth and crisp UI with animations or transitions that imply we know our way around tecchnology is always helpful - but a Clean and responsive UI is most important.
Nice to have
• Reactive and animated transitions through sections or pages - not overdone - adds a professional feel to the site
Should not have
• We don't want too many colours, and we don't want it too dark - we want a monochrome theme, with accents of colour when relevant

```html
<!DOCTYPE html>
<html lang="en">
<head>
<meta charset="utf-8">
<title>Vendro Consulting</title>
<link rel="stylesheet" href="https://fonts.googleapis.com/css2?family=Montserrat:wght@300;400;500;600;700&family=Poppins:wght@400;600;700&display=swap">
<style>
:root{
  --blue:#0a6fc2;
  --blue-bright:#1c86db;
  --band:#1f7ccb;
  --ink:#1c1c1c;
  --body:#555;
  --mist:#f4f4f4;
  --white:#fff;
  --night:#0b0b0b;
}
*{margin:0;padding:0;box-sizing:border-box}
html,body{width:1200px;height:4205px;overflow:hidden}
body{font-family:"Montserrat",sans-serif;color:var(--ink);background:var(--white)}
a{text-decoration:none}
section,header,footer{position:relative;width:1200px;overflow:hidden}
.abs{position:absolute}
.btn{position:absolute;display:flex;align-items:center;justify-content:center;background:var(--blue);color:var(--white);font-size:12px;font-weight:600;text-decoration:none}
.btn.pill{border-radius:4px 16px 4px 16px;font-size:11px;letter-spacing:.3px}
.section-title{position:absolute;left:0;width:1200px;text-align:center;font-size:40px;font-weight:300;color:var(--ink)}
.section-title b{font-weight:600;color:var(--blue)}

/* hero */
.hero{height:591px;background:linear-gradient(100deg,#151515 0%,#2b2b2b 40%,#5a5a5a 68%,#2e2e2e 100%)}
.hero-photo{position:absolute;left:520px;top:0;width:680px;height:591px;background:radial-gradient(ellipse at 55% 45%,#8a8a8a 0%,#4d4d4d 45%,rgba(30,30,30,0) 80%)}
.brand{position:absolute;display:flex;align-items:center;gap:10px;color:var(--blue-bright);font-family:"Poppins",sans-serif;font-weight:600;letter-spacing:1px;text-decoration:none}
.brand i{display:block;background:var(--blue-bright)}
.hero .brand{left:160px;top:20px;font-size:40px;line-height:48px}
.hero .brand i{width:40px;height:40px}
.nav{position:absolute;top:31px;display:flex;color:var(--white);font-size:13px}
.nav a{position:absolute;color:var(--white);text-decoration:none;white-space:nowrap}
.nav .active:after{content:"";position:absolute;left:50%;top:26px;width:14px;height:3px;margin-left:-7px;background:var(--blue-bright)}
.hero h1{position:absolute;left:163px;top:172px;font-family:"Poppins",sans-serif;font-size:29px;line-height:46px;font-weight:700;color:var(--white)}
.hero h1 span{color:var(--blue-bright)}
.hero .lede{position:absolute;left:163px;top:320px;font-size:17px;line-height:31px;color:#eee;letter-spacing:.3px}
.call{position:absolute;left:310px;top:400px;display:flex;gap:14px;color:var(--white)}
.call small{display:block;font-size:10px;letter-spacing:.5px}
.call strong{display:block;font-size:17px;font-weight:600}
.dots{position:absolute;left:168px;top:499px;display:flex;gap:5px}
.dots i{display:block;width:14px;height:3px;background:#777}
.dots i:first-child{background:var(--blue-bright)}

/* about */
.about{height:609px}
.about h2{position:absolute;left:607px;top:736px;font-size:39px;font-weight:300}
.about h2 b{font-weight:600;color:var(--blue)}
.about p.copy{position:absolute;left:607px;top:804px;width:445px;font-size:10.3px;line-height:19.5px;color:var(--body)}
.quote{position:absolute;left:607px;top:912px;width:410px;font-size:13.5px;line-height:21px;font-weight:600;color:var(--blue)}
.qmark{position:absolute;font-family:"Poppins",sans-serif;font-size:40px;font-weight:700;color:var(--blue);line-height:1}

/* services */
.services{height:573px;background:var(--mist)}
.service h3{position:absolute;font-size:15px;font-weight:600;letter-spacing:.3px;color:var(--ink)}
.service p{position:absolute;width:300px;font-size:10.2px;line-height:19px;color:var(--body)}
.service ul{position:absolute;list-style:none;display:grid;grid-template-columns:130px 130px;row-gap:7px;font-size:11px;color:var(--body)}
.service li{position:relative;padding-left:22px;line-height:18px}
.service li:before{content:"";position:absolute;left:0;top:6px;width:6px;height:6px;border-radius:50%;background:var(--blue)}

/* why */
.why{height:451px;background:linear-gradient(180deg,#2584d2 0%,#1b76c4 100%)}
.why h2{position:absolute;left:0;top:145px;width:1200px;text-align:center;font-size:39px;font-weight:300;color:var(--white)}
.why h2 b{font-weight:600}
.num{position:absolute;font-family:"Montserrat",sans-serif;font-size:64px;font-weight:300;color:transparent;-webkit-text-stroke:1px rgba(255,255,255,.55)}
.reason{position:absolute;width:260px;text-align:center;font-size:15px;line-height:20px;font-weight:600;color:var(--white)}

/* blogs */
.blogs{height:626px}
.card{position:absolute;top:141px;width:283px;height:408px;background:var(--white);box-shadow:0 4px 14px rgba(0,0,0,.09)}
.card .thumb{height:184px}
.card time{position:absolute;left:23px;top:203px;font-size:11px;font-weight:600;color:var(--blue)}
.card h3{position:absolute;left:23px;top:224px;width:240px;font-size:14px;line-height:19px;font-weight:600}
.card p{position:absolute;left:23px;top:268px;width:240px;font-size:10.5px;line-height:19px;color:var(--body)}
.card .btn{left:23px;top:359px;width:119px;height:33px}

/* mission */
.mission{height:486px;background:linear-gradient(120deg,#4b5560 0%,#6a6258 35%,#3f5368 65%,#5d6a55 100%)}
.mission h2{position:absolute;left:0;top:140px;width:1200px;text-align:center;font-size:39px;font-weight:300}
.mission h2 b{font-weight:600;color:var(--blue)}
.mission p{position:absolute;left:440px;top:196px;width:320px;text-align:center;font-size:10.5px;line-height:24px;color:#333;font-weight:500}

/* contact */
.contact{height:567px;background:linear-gradient(180deg,#f6f6f6 0%,#fbfbfb 60%,#f3f3f3 100%)}
.contact h2{position:absolute;left:0;top:58px;width:1200px;text-align:center;font-size:39px;font-weight:300}
.contact h2 b{font-weight:600;color:var(--blue)}
.contact .intro{position:absolute;left:380px;top:118px;width:440px;text-align:center;font-size:11px;line-height:18px;color:var(--body)}
.field{position:absolute;background:var(--white);box-shadow:0 2px 8px rgba(0,0,0,.07);font-size:11px;color:var(--blue);padding:10px 14px}

/* footer */
.footer{height:302px}
.footer .brand{left:492px;top:35px;font-size:44px;line-height:52px;color:var(--white)}
.footer .brand i{width:46px;height:46px;background:var(--white)}
.rule{position:absolute;left:183px;width:833px;height:1px;background:#3a3a3a}
.fnav a{position:absolute;top:137px;font-size:11px;color:var(--white);text-decoration:none;transform:translateX(-50%)}
.contact-item{position:absolute;top:188px;display:flex;gap:12px;align-items:center;color:var(--white);font-size:11px;line-height:16px}
.contact-item b{display:block;font-weight:600}
.social{position:absolute;top:193px;width:30px;height:30px;border:1.5px solid var(--white);border-radius:50%}
.copyright{position:absolute;left:0;top:264px;width:1200px;text-align:center;font-size:10.5px;color:#ddd}
</style>
</head>
<body>

<header class="hero">
  <div class="hero-photo" role="img" aria-label="Black and white photo of two business people shaking hands across a desk"></div>
  <a class="brand" href="#"><i></i>VENDRO</a>
  <nav class="nav">
    <a class="active" style="left:482px">Home</a>
    <a style="left:545px">About</a>
    <a style="left:610px">Services</a>
    <a style="left:692px">Team</a>
    <a style="left:753px">Contact Us</a>
  </nav>
  <a class="btn" href="#contact" style="left:849px;top:23px;width:191px;height:33px;font-weight:500;font-size:12.5px">Request A Consultation</a>
  <h1>VENDRO Is A <span>Premier Consulting</span><br>Firm That Specialises In <span>Aiding</span><br><span>Global Corporations</span></h1>
  <p class="lede">And Emerging Businesses To Enter And Scale Within<br>Africa’s Dynamic Markets</p>
  <a class="btn" href="#contact" style="left:162px;top:402px;width:116px;height:39px;font-size:13px;font-weight:500">Contact US</a>
  <div class="call">
    <svg width="30" height="32" viewBox="0 0 24 24" fill="none" stroke="#1c86db" stroke-width="1.6"><path d="M6 3l3 4-2 2c1 3 4 6 7 7l2-2 4 3-2 3c-7 0-14-7-14-14z"/><path d="M14 3a7 7 0 017 7M14 6a4 4 0 014 4"/></svg>
    <div><small>CALL NOW :</small><strong>+1 555-014-2290</strong></div>
  </div>
  <div class="dots"><i></i><i></i><i></i></div>
</header>

<section class="about" style="height:609px">
  <svg class="abs" style="left:0;top:0" width="600" height="609" viewBox="0 591 600 609">
    <defs><filter id="soft" x="-20%" y="-20%" width="140%" height="140%"><feDropShadow dx="0" dy="3" stdDeviation="5" flood-opacity=".15"/></filter></defs>
    <g role="img" aria-label="Photo of hands working at a laptop with data overlays">
      <polygon points="270,670 387,731 387,854 270,915 152,854 152,731" fill="#3d6794"/>
    </g>
    <g role="img" aria-label="Photo of two consultants talking in an office">
      <polygon points="404,800 485,847 485,941 404,988 322,941 322,847" fill="#6b7f93"/>
    </g>
    <g role="img" aria-label="Photo of business people shaking hands">
      <polygon points="313,955 397,1001 397,1092 313,1138 229,1092 229,1001" fill="#4c4c52"/>
    </g>
    <polygon points="455,691 505,719 505,775 455,803 405,775 405,719" fill="#0a6fc2"/>
    <text x="455" y="744" font-family="Montserrat" font-size="13" font-weight="500" fill="#fff" text-anchor="middle">LOREM</text>
    <text x="455" y="761" font-family="Montserrat" font-size="13" font-weight="500" fill="#fff" text-anchor="middle">IPSUM</text>
    <polygon points="194,878 245,906 245,962 194,990 142,962 142,906" fill="#fff" filter="url(#soft)"/>
    <text x="194" y="929" font-family="Montserrat" font-size="13" font-weight="500" fill="#0a6fc2" text-anchor="middle">LOREM</text>
    <text x="194" y="946" font-family="Montserrat" font-size="13" font-weight="500" fill="#0a6fc2" text-anchor="middle">IPSUM</text>
    <polygon points="467,980 518,1008 518,1066 467,1094 416,1066 416,1008" fill="#fff" stroke="#1c86db" stroke-width="1.3"/>
    <text x="467" y="1033" font-family="Montserrat" font-size="13" font-weight="500" fill="#0a6fc2" text-anchor="middle">LOREM</text>
    <text x="467" y="1050" font-family="Montserrat" font-size="13" font-weight="500" fill="#0a6fc2" text-anchor="middle">IPSUM</text>
  </svg>
  <div style="position:absolute;left:0;top:-591px;width:1200px;height:1200px">
    <h2>About <b>Vendro Consulting.</b></h2>
    <p class="copy">Maecenas tempus, leo nec dictum lacinia, lacus nisl ullamcorper ipsum, at blandit leo enim in libero. Morbi at rutrum massa, et tincidunt nisl.Suspendisse ac auctor nibh, eget rutrum enim. In in fringilla sapien, a rutrum quam. Nullam id libero quam. Aliquam eget hendrerit lorem.</p>
    <span class="qmark" style="left:583px;top:893px">“</span>
    <p class="quote">Maecenas tempus, leo nec dictum lacinia, lacus nisl ullamcorper ipsum, at blandit leo enim in libero. Morbi at rutrum massa, et tincidunt nisi.</p>
    <span class="qmark" style="left:836px;top:968px">”</span>
    <a class="btn pill" href="#" style="left:607px;top:1006px;width:172px;height:33px">Request A Consultation</a>
  </div>
</section>

<section class="services">
  <h2 class="section-title" style="top:36px">Our <b>Services</b></h2>
  <svg class="abs" style="left:0;top:0" width="1200" height="573" viewBox="0 1200 1200 573" fill="none">
    <g stroke="#b9c9d8" stroke-dasharray="4 3" stroke-width="1.2">
      <path d="M555 1356 H585 V1690"/><path d="M647 1356 H615 V1690"/>
      <path d="M555 1566 H585"/><path d="M647 1566 H615"/>
    </g>
    <g fill="#fff" stroke="#2a86d6" stroke-width="1.4">
      <polygon points="521,1320 555,1338 555,1374 521,1392 487,1374 487,1338"/>
      <polygon points="681,1320 715,1338 715,1374 681,1392 647,1374 647,1338"/>
      <polygon points="521,1528 555,1547 555,1585 521,1604 487,1585 487,1547"/>
      <polygon points="681,1528 715,1547 715,1585 681,1604 647,1585 647,1547"/>
    </g>
    <g fill="#fff" stroke="#cfe0ef" stroke-width="1">
      <circle cx="548" cy="1356" r="3"/><circle cx="654" cy="1356" r="3"/>
      <circle cx="548" cy="1566" r="3"/><circle cx="654" cy="1566" r="3"/>
    </g>
    <g fill="#0a6fc2">
      <path d="M521 1343a10 10 0 00-10 10c0 8 10 17 10 17s10-9 10-17a10 10 0 00-10-10zm0 14a4 4 0 110-8 4 4 0 010 8z"/>
      <rect x="670" y="1347" width="22" height="16" rx="2"/><rect x="677" y="1343" width="8" height="5" rx="1" fill="none" stroke="#0a6fc2" stroke-width="2"/>
      <circle cx="514" cy="1570" r="8"/><circle cx="528" cy="1560" r="7" fill="none" stroke="#0a6fc2" stroke-width="2"/>
      <rect x="673" y="1552" width="18" height="24" rx="2" fill="none" stroke="#0a6fc2" stroke-width="2"/>
      <path d="M677 1560h10M677 1565h10M677 1570h6" stroke="#0a6fc2" stroke-width="1.6"/>
    </g>
    <polygon points="600,1679 679,1724 679,1810 600,1855 521,1810 521,1724" fill="#fff" stroke="#bcd6ee" stroke-width="2"/>
    <polygon points="600,1690 668,1730 668,1804 600,1844 532,1804 532,1730" fill="#9ec6ea"/>
    <polygon points="600,1697 662,1733 662,1801 600,1837 538,1801 538,1733" fill="#0a6fc2"/>
    <g stroke="#fff" stroke-width="2" fill="none">
      <path d="M593 1752a9 9 0 1114 0c-2 2-2 4-2 5h-10c0-1 0-3-2-5z"/><path d="M596 1761h8M597 1765h6"/>
      <path d="M600 1722v4M585 1728l3 3M615 1728l-3 3M580 1742h4M616 1742h4"/>
    </g>
    <text x="600" y="1785" font-family="Montserrat" font-size="15" font-weight="500" fill="#fff" text-anchor="middle">LOREM</text>
    <text x="600" y="1808" font-family="Montserrat" font-size="15" font-weight="500" fill="#fff" text-anchor="middle">IPSUM</text>
  </svg>

  <div class="service">
    <h3 style="left:149px;top:112px">DEDICATION TO AFRICA</h3>
    <p style="left:149px;top:137px">Maecenas tempus, leo nec dictum lacinia, lacus nisl ullamcorper ipsum, at blandit leo enim in libero.Morbi at rutrum massa, et tincidunt nisi.Suspendisse ac.</p>
    <ul style="left:152px;top:202px"><li>Lorem Ipsum</li><li>Lorem Ipsum</li><li>Lorem Ipsum</li><li>Lorem Ipsum</li><li>Lorem Ipsum</li><li>Lorem Ipsum</li></ul>
  </div>
  <div class="service">
    <h3 style="left:753px;top:112px">ASSISTING MULTINATIONAL FIRMS</h3>
    <p style="left:753px;top:137px">Maecenas tempus, leo nec dictum lacinia, lacus nisl ullamcorper ipsum, at blandit leo enim in libero.Morbi at rutrum massa, et tincidunt nisi.Suspendisse ac.</p>
    <ul style="left:756px;top:202px"><li>Lorem Ipsum</li><li>Lorem Ipsum</li><li>Lorem Ipsum</li><li>Lorem Ipsum</li><li>Lorem Ipsum</li><li>Lorem Ipsum</li></ul>
  </div>
  <div class="service">
    <h3 style="left:149px;top:332px">CONSULTING</h3>
    <p style="left:149px;top:358px">Maecenas tempus, leo nec dictum lacinia, lacus nisl ullamcorper ipsum, at blandit leo enim in libero.Morbi at rutrum massa, et tincidunt nisi.Suspendisse ac.</p>
    <ul style="left:152px;top:422px"><li>Lorem Ipsum</li><li>Lorem Ipsum</li><li>Lorem Ipsum</li><li>Lorem Ipsum</li><li>Lorem Ipsum</li><li>Lorem Ipsum</li></ul>
  </div>
  <div class="service">
    <h3 style="left:753px;top:332px">LOREM IPSUM DOLOR</h3>
    <p style="left:753px;top:358px">Maecenas tempus, leo nec dictum lacinia, lacus nisl ullamcorper ipsum, at blandit leo enim in libero.Morbi at rutrum massa, et tincidunt nisi.Suspendisse ac.</p>
    <ul style="left:756px;top:422px"><li>Lorem Ipsum</li><li>Lorem Ipsum</li><li>Lorem Ipsum</li><li>Lorem Ipsum</li><li>Lorem Ipsum</li><li>Lorem Ipsum</li></ul>
  </div>
</section>

<section class="why">
  <svg class="abs" style="left:0;top:0" width="1200" height="451" viewBox="0 1773 1200 451" fill="none">
    <polygon points="600,1679 679,1724 679,1810 600,1855 521,1810 521,1724" fill="#fff" stroke="#bcd6ee" stroke-width="2"/>
    <polygon points="600,1690 668,1730 668,1804 600,1844 532,1804 532,1730" fill="#9ec6ea"/>
    <polygon points="600,1697 662,1733 662,1801 600,1837 538,1801 538,1733" fill="#0a6fc2"/>
    <g stroke="#fff" stroke-width="2" fill="none">
      <path d="M593 1752a9 9 0 1114 0c-2 2-2 4-2 5h-10c0-1 0-3-2-5z"/><path d="M596 1761h8M597 1765h6"/>
    </g>
    <text x="600" y="1785" font-family="Montserrat" font-size="15" font-weight="500" fill="#fff" text-anchor="middle">LOREM</text>
    <text x="600" y="1808" font-family="Montserrat" font-size="15" font-weight="500" fill="#fff" text-anchor="middle">IPSUM</text>
    <path d="M600 1855v7" stroke="#fff" stroke-width="1.4"/>
    <circle cx="600" cy="1870" r="8" stroke="#fff" stroke-width="1.5"/><circle cx="600" cy="1870" r="3.5" fill="#fff"/>
    <path d="M600 1878v34M595 1907l5 6 5-6" stroke="#fff" stroke-width="1.4"/>
    <path d="M286 2095 V2018 Q286 2009 295 2009 H902 Q911 2009 911 2018 V2095 M600 2030 V2095" stroke="rgba(255,255,255,.75)" stroke-dasharray="5 4" stroke-width="1.2"/>
    <rect x="576" y="1989" width="48" height="42" rx="21" fill="#1f7ccb" stroke="rgba(255,255,255,.8)" stroke-width="1.2"/>
    <text x="600" y="2007" font-family="Montserrat" font-size="10" fill="#fff" text-anchor="middle">Lorem</text>
    <text x="600" y="2021" font-family="Montserrat" font-size="10" fill="#fff" text-anchor="middle">Ipsum</text>
    <g fill="#fff"><circle cx="286" cy="2095" r="5"/><circle cx="600" cy="2095" r="5"/><circle cx="911" cy="2095" r="5"/></g>
  </svg>
  <h2>Why <b>Choose Us?</b></h2>
  <span class="num" style="left:230px;top:262px">1</span>
  <span class="num" style="left:527px;top:262px">2</span>
  <span class="num" style="left:840px;top:262px">3</span>
  <p class="reason" style="left:156px;top:348px">Lorem Ipsum Dolor Sit Amet, Consectetur</p>
  <p class="reason" style="left:470px;top:348px">Lorem Ipsum Dolor Sit Amet, Consectetur</p>
  <p class="reason" style="left:781px;top:348px">Lorem Ipsum Dolor Sit Amet, Consectetur</p>
</section>

<section class="blogs">
  <h2 class="section-title" style="top:62px">Our <b>Blogs</b></h2>
  <article class="card" style="left:150px">
    <div class="thumb" role="img" aria-label="Photo of two men in conversation over coffee" style="background:linear-gradient(135deg,#c9c6c0,#7b7f84)"></div>
    <time>10 JUNE 2023</time>
    <h3>Lorem Ipsum Dolor Sit Amet, Consectetur</h3>
    <p>Maecenas tempus, leo nec dictum lacinia, lacus nisl ullamcorper ipsum, at blandit leo enim in libero.Morbi at rutrum massa, et tincidunt nisi.Suspendisse ac.</p>
    <a class="btn pill" href="#">READ MORE</a>
  </article>
  <article class="card" style="left:459px">
    <div class="thumb" role="img" aria-label="Photo of a laptop with financial data overlays" style="background:linear-gradient(135deg,#2c4c74,#5d86b3)"></div>
    <time>10 JUNE 2023</time>
    <h3>Lorem Ipsum Dolor Sit Amet, Consectetur</h3>
    <p>Maecenas tempus, leo nec dictum lacinia, lacus nisl ullamcorper ipsum, at blandit leo enim in libero.Morbi at rutrum massa, et tincidunt nisi.Suspendisse ac.</p>
    <a class="btn pill" href="#">READ MORE</a>
  </article>
  <article class="card" style="left:767px">
    <div class="thumb" role="img" aria-label="Photo of a hand holding a mobile phone by a money transfer sign" style="background:linear-gradient(135deg,#3a3f3b,#7b8b7e 60%,#3d6a45)"></div>
    <time>10 JUNE 2023</time>
    <h3>Lorem Ipsum Dolor Sit Amet, Consectetur</h3>
    <p>Maecenas tempus, leo nec dictum lacinia, lacus nisl ullamcorper ipsum, at blandit leo enim in libero.Morbi at rutrum massa, et tincidunt nisi.Suspendisse ac.</p>
    <a class="btn pill" href="#">READ MORE</a>
  </article>
</section>

<section class="mission" role="img" aria-label="Photo of a busy African street market with stalls and umbrellas">
  <svg class="abs" style="left:0;top:0" width="1200" height="486" viewBox="0 0 1200 486">
    <path d="M586 34 Q600 26 614 34 L776 127 Q790 135 790 151 V336 Q790 352 776 360 L614 453 Q600 461 586 453 L424 360 Q410 352 410 336 V151 Q410 135 424 127 Z" fill="#fff"/>
    <circle cx="600" cy="354" r="12" fill="#0a6fc2"/>
    <path d="M594 354h11M600 348l6 6-6 6" stroke="#fff" stroke-width="2" fill="none"/>
  </svg>
  <h2>Our <b>Mission</b></h2>
  <p>Maecenas tempus, leo nec dictum lacinia, lacus nisi ullamcorper ipsum, at blandit leo enim in libero. Morbi at rutrum massa, et tincidunt nisl.Suspendisse ac auctor nibh, eget rutrum enim. In in fringilla sapien, a rutrum quam. Nullam id libero quam. Aliquam.</p>
</section>

<section class="contact" id="contact">
  <h2>Contact <b>Us</b></h2>
  <p class="intro">Maecenas tempus, leo nec dictum lacinia, lacus nisl ullamcorper ipsum, at blandit leo enim in libero.</p>
  <div class="field" style="left:382px;top:173px;width:211px;height:33px">First Name</div>
  <div class="field" style="left:607px;top:173px;width:210px;height:33px">Last Name</div>
  <div class="field" style="left:382px;top:219px;width:211px;height:33px">Email</div>
  <div class="field" style="left:607px;top:219px;width:210px;height:33px">Phone</div>
  <div class="field" style="left:382px;top:265px;width:435px;height:132px">Message</div>
  <a class="btn pill" href="#" style="left:541px;top:421px;width:117px;height:32px">SUBMIT</a>
</section>

<footer class="footer" style="margin-top:-36px;height:338px">
  <svg class="abs" style="left:0;top:0" width="1200" height="338" viewBox="0 0 1200 338"><path d="M0 85 Q600 -10 1200 85 V338 H0Z" fill="#0b0b0b"/></svg>
  <div style="position:absolute;left:0;top:36px;width:1200px;height:302px">
    <a class="brand" href="#"><i></i>VENDRO</a>
    <div class="rule" style="top:119px"></div>
    <nav class="fnav">
      <a style="left:354px">Home</a><a style="left:470px">About</a><a style="left:594px">Services</a><a style="left:718px">Team</a><a style="left:839px">Contact</a>
    </nav>
    <div class="rule" style="top:174px"></div>
    <div class="contact-item" style="left:182px">
      <svg width="28" height="28" viewBox="0 0 24 24" fill="none" stroke="#fff" stroke-width="1.4"><path d="M6 3l3 4-2 2c1 3 4 6 7 7l2-2 4 3-2 3c-7 0-14-7-14-14z"/></svg>
      <div><b>Phone</b>555-014-7731</div>
    </div>
    <div class="contact-item" style="left:496px">
      <svg width="30" height="28" viewBox="0 0 24 24" fill="none" stroke="#fff" stroke-width="1.4"><path d="M2 11L22 3l-6 18-5-7-9-3z"/><path d="M11 14l11-11"/></svg>
      <div><b>Email</b>info@vendroconsulting.example</div>
    </div>
    <span class="social" style="left:867px" aria-label="Social profile"></span>
    <span class="social" style="left:906px" aria-label="Picsnap"></span>
    <span class="social" style="left:945px" aria-label="Social profile"></span>
    <span class="social" style="left:984px" aria-label="Workhive"></span>
    <div class="rule" style="top:245px"></div>
    <p class="copyright">© 2023 Vendro Consulting. All Rights Reserved.</p>
  </div>
</footer>

</body>
</html>
```